Need web redesign for cybersecurity startup whose mission is to make robust cybersecurity protection

We need a web redesign for Velundra, a cyber security startup. We already have a logo and website but we’re looking for a redesign to reflect the new messaging and positioning of the company – and to update our look with a more polished feel. We’re looking for clean, powerful, confident designs that easily communicate the problems within the cybersecurity space and how Velundra is the answer to those problems.

We can have the long-scrolling stripe layout for the home page, but we don’t want a bunch of interior pages with the same long-scroll format. We’d like to do something a little different and easier to navigate.

Velundra’s products simplify and automate cybersecurity defense so non-experts can successfully protect their information and focus on their business. Velundra’s mission is to provide proactive cybersecurity protection that is easy to use, easy to implement and easy to afford. The designs should reflect this populist message as well as confidence and maybe a little irreverence. Additional key words to describe the company are: secure, protection, easy, everyone.

Velundra offers multiple security products which can both be purchased directly from their site. They provide the world’s most widely used WAF rule set for Wardplex as well as Velundra Guarded Linux (VGL) and Velundra Guarded Linux Kernels to protect Linux servers, IoT devices and Podlane containers.

Target Market(s)

IT leaders in small and mid-sized businesses, hosting providers, and enterprise dev ops, product and security groups

Industry/Entity Type

Security

Number of Pages Required

5+ page

Font styles to use
Serif
Sans Serif

Requirements
Must have
• - We can have the long-scrolling stripe layout for the home page, but we don’t want a bunch of interior pages with the same long-scroll format. We’d like to do something a little different and easier to navigate.
• - Clean, powerful, confident designs
• - Real imagery coupled with line designs
Nice to have
• Specific icons to be used for all marketing and web materials for each product:
• - Velund Guarded for Linux (VG/L)
• - WardPlex Rules
• - Velundra Guarded Linux Kernels
• - KRIVE - Commercial Support
• - Guarded OS for Podlane
• - Guarded Apps for Podlane
Should not have
• - No typical imagery for cybersecurity such as binary code, hooded figures, etc.

```html
<!DOCTYPE html>
<html lang="en">
<head>
<meta charset="utf-8">
<title>Velundra — Linux Server Protection</title>
<link href="https://fonts.googleapis.com/css2?family=Roboto:wght@400;500;700&family=Gloria+Hallelujah&display=swap" rel="stylesheet">
<style>
  :root {
    --accent-red: #e8392f;
    --navy: #1d2a48;
    --navy-deep: #172238;
    --globe-line: #2f6ea8;
    --ink: #1f1f1f;
    --ink-soft: #4a4a4a;
    --muted: #7b7f86;
    --bar-bg: #eef0f3;
    --white: #ffffff;
    --btn-dark: #2a2a2a;
    --forest: #4f6b35;
    --forest-light: #8aa05a;
  }
  * { box-sizing: border-box; margin: 0; padding: 0; }
  html, body { width: 1200px; height: 676px; overflow: hidden; background: var(--white); }
  body { font-family: "Roboto", Arial, sans-serif; color: var(--ink); }

  .page { position: relative; width: 1200px; height: 676px; overflow: hidden; }
  .top-stripe { height: 4px; background: var(--accent-red); }

  .site-header {
    height: 76px; display: flex; align-items: center;
    padding: 0 44px; background: var(--white);
  }
  .brand { display: flex; align-items: center; gap: 8px; width: 380px; }
  .brand-dot { width: 18px; height: 18px; border-radius: 50%; background: var(--accent-red); }
  .brand-name { font-weight: 700; font-size: 15px; letter-spacing: 1px; color: var(--ink); }
  .main-nav { display: flex; gap: 38px; font-size: 14px; color: var(--ink); }
  .header-actions { margin-left: auto; display: flex; gap: 8px; }
  .btn {
    display: inline-flex; align-items: center; gap: 5px;
    height: 30px; padding: 0 12px; border-radius: 4px;
    font-size: 13px; font-weight: 700; color: var(--white);
  }
  .btn-chat { background: var(--btn-dark); }
  .btn-trial { background: var(--accent-red); }

  .hero {
    position: relative; height: 440px;
    background: radial-gradient(ellipse at 70% 40%, var(--navy) 0%, var(--navy-deep) 100%);
  }
  .hero-globe {
    position: absolute; left: 130px; top: 48px; width: 360px; height: 360px; border-radius: 50%;
    background: radial-gradient(circle at 45% 40%, rgba(47,110,168,0.35) 0%, rgba(47,110,168,0.15) 60%, rgba(47,110,168,0) 72%);
    border: 1px solid rgba(47,110,168,0.5);
  }
  .hero-copy { position: absolute; left: 520px; top: 160px; width: 440px; text-align: center; }
  .hero-title {
    font-family: "Gloria Hallelujah", cursive; font-weight: 400;
    font-size: 24px; line-height: 1.35; color: var(--white); letter-spacing: 1px;
  }
  .hero-tags { margin-top: 22px; display: flex; justify-content: center; gap: 8px; }
  .hero-tag {
    border: 2px solid var(--white); border-radius: 5px; padding: 5px 12px;
    font-size: 12px; font-weight: 500; color: var(--white);
  }

  .info-bar {
    height: 36px; background: var(--bar-bg); display: flex; align-items: center;
    padding: 0 44px; font-size: 12px; color: var(--muted);
  }
  .contact-item { display: flex; align-items: center; gap: 6px; margin-right: 30px; }
  .learn-more { margin-left: auto; display: flex; gap: 22px; align-items: center; }
  .learn-label { color: var(--ink-soft); font-weight: 500; }

  .intro { display: flex; padding: 16px 44px 0 80px; gap: 60px; }
  .intro-text { width: 560px; text-align: center; }
  .intro-title { font-size: 22px; font-weight: 500; color: var(--ink); }
  .intro-title em { font-style: normal; color: var(--accent-red); }
  .intro-rule { margin: 10px 0 16px; border-top: 2px dotted var(--accent-red); }
  .intro-body { font-size: 13px; line-height: 1.45; color: var(--ink-soft); }
  .intro-body + .intro-body { margin-top: 10px; }
  .intro-video {
    position: relative; width: 330px; height: 130px;
    background: linear-gradient(135deg, var(--forest) 0%, var(--forest-light) 60%, var(--forest) 100%);
  }
  .play-control {
    position: absolute; left: 50%; top: 60%; transform: translate(-50%, -50%);
    width: 44px; height: 44px; border-radius: 50%; background: rgba(0,0,0,0.55);
    display: flex; align-items: center; justify-content: center;
  }
</style>
</head>
<body>
<div class="page">
  <div class="top-stripe"></div>

  <header class="site-header">
    <div class="brand">
      <span class="brand-dot"></span>
      <span class="brand-name">VELUNDRA</span>
    </div>
    <nav class="main-nav">
      <span>Our Company</span>
      <span>Products</span>
      <span>Support</span>
      <span>Buy Now</span>
    </nav>
    <div class="header-actions">
      <span class="btn btn-chat">
        <svg width="13" height="12" viewBox="0 0 13 12"><path d="M6.5 1C3.5 1 1 2.9 1 5.2c0 1.2.7 2.3 1.8 3L2.3 11l3-2c.4.1.8.1 1.2.1 3 0 5.5-1.9 5.5-4.2S9.5 1 6.5 1z" fill="none" stroke="#fff" stroke-width="1.4"/></svg>
        Chat
      </span>
      <span class="btn btn-trial">Free Trial</span>
    </div>
  </header>

  <section class="hero">
    <div class="hero-globe" role="img" aria-label="Glowing wireframe globe of connected network points against a starry night sky"></div>
    <div class="hero-copy">
      <h1 class="hero-title">Don't Be the Next Cyber Victim.<br>Harden Your Shell Now</h1>
      <div class="hero-tags">
        <span class="hero-tag">WAF Rules</span>
        <span class="hero-tag">Linux Servers</span>
        <span class="hero-tag">IoT Devices</span>
      </div>
    </div>
  </section>

  <div class="info-bar">
    <span class="contact-item">
      <svg width="11" height="11" viewBox="0 0 24 24"><path d="M6.6 10.8a15.1 15.1 0 006.6 6.6l2.2-2.2c.3-.3.7-.4 1-.2 1.1.4 2.3.6 3.6.6.6 0 1 .4 1 1V20c0 .6-.4 1-1 1A17 17 0 013 4c0-.6.4-1 1-1h3.5c.6 0 1 .4 1 1 0 1.3.2 2.5.6 3.6.1.3 0 .7-.2 1z" fill="#7b7f86"/></svg>
      +1 555 014 72 38
    </span>
    <span class="contact-item">
      <svg width="12" height="9" viewBox="0 0 12 9"><rect x="0" y="0" width="12" height="9" rx="1" fill="#7b7f86"/><path d="M0.5 0.8L6 5l5.5-4.2" fill="none" stroke="#eef0f3" stroke-width="1.2"/></svg>
      hello@velundra.example
    </span>
    <nav class="learn-more">
      <span class="learn-label">Learn More:</span>
      <span>Blog</span>
      <span>Careers</span>
      <span>Threat Map</span>
      <span>Testimonials</span>
      <span>Contact Us</span>
      <svg width="12" height="12" viewBox="0 0 12 12"><circle cx="5" cy="5" r="3.6" fill="none" stroke="#4a4a4a" stroke-width="1.6"/><path d="M7.7 7.7L11 11" stroke="#4a4a4a" stroke-width="1.8"/></svg>
    </nav>
  </div>

  <section class="intro">
    <div class="intro-text">
      <h2 class="intro-title">Linux Server Protection for <em>Everyone and Everything</em></h2>
      <div class="intro-rule"></div>
      <p class="intro-body">Cyber attacks happen. The question is, are you ready? For too many mid-sized and small business the answer is no because they don't think cyber protection is accessible or made for their needs.</p>
      <p class="intro-body">Even enterprises often are left unprotected by outdated tools and complex setups across their teams.</p>
    </div>
    <div class="intro-video" role="img" aria-label="Video thumbnail: aerial view of a winding road through a green forest">
      <span class="play-control">
        <svg width="16" height="18" viewBox="0 0 16 18"><path d="M2 1l13 8-13 8z" fill="#fff"/></svg>
      </span>
    </div>
  </section>
</div>
</body>
</html>
```